Financial investment & advisory business needs a powerpoint design

We need a powerpoint design incorporating the logo (and colours) and relating to the business card design we already have. The company is a boutique financial investment and advisory business called Brevora Holdings Pty Ltd based in Australia. The final design should communicate innovative advice and financial safety and growth. A young, contemporary but experienced, professional business.

Target Market(s)

Companies listed or wishing to list on the Tarrowin Stock Exchange and Professional and Institutional Investors.

Industry/Entity Type

Finance

Requirements
Must have
• Incorporate the logo and colours. Be similar/relate to the business card design.
Nice to have
Should not have
• Do not deviate from the logo colours.
• Do not use black background or invert the logo.
• Do not deviate from the business card design too much.

```html
<!DOCTYPE html>
<html lang="en">
<head>
<meta charset="utf-8">
<title>Brevora Holdings – Presentation Slides</title>
<link href="https://fonts.googleapis.com/css2?family=Open+Sans:wght@400;600;700&display=swap" rel="stylesheet">
<style>
  :root{
    --blue:#3b5ca8;
    --blue-soft:#5a78bd;
    --grey:#8a8a8a;
    --grey-mid:#9b9b9b;
    --grey-light:#c9c9c9;
    --dark:#4f4f4f;
    --band:#7f7f7f;
    --frame:#c4c4c4;
    --canvas:#ffffff;
    --sky-top:#2d5fae;
    --sky-mid:#7fa7d8;
    --city:#8d97a3;
    --ground:#4a525c;
  }
  *{margin:0;padding:0;box-sizing:border-box}
  html,body{width:1200px;height:512px;overflow:hidden;background:var(--canvas)}
  body{position:relative;font-family:"Open Sans",Arial,sans-serif}
  .deck{position:relative;width:1200px;height:512px}
  .slide{position:absolute;width:294px;height:165px;background:#fff;outline:1px solid var(--frame);overflow:hidden}
  .slide svg{position:absolute;left:0;top:0}
  .photo{position:absolute;left:0;top:0;width:100%;height:100%;
    background:linear-gradient(180deg,var(--sky-top) 0%,var(--sky-mid) 42%,var(--city) 68%,var(--ground) 100%)}
  .photo--sky{left:150px;width:144px;background:linear-gradient(160deg,#3d78c6 0%,#8fb5e0 45%,#e6eef8 70%,#9fbfe4 100%)}
  .col-1{left:3px}.col-2{left:302px}.col-3{left:601px}.col-4{left:900px}
  .row-1{top:2px}.row-2{top:173px}.row-3{top:344px}

  svg text{font-family:"Open Sans",Arial,sans-serif}
  .t-title{font-size:9.5px;font-weight:600;fill:var(--dark)}
  .t-title .accent{fill:var(--blue);font-weight:700}
  .t-sub{font-size:4.4px;fill:var(--grey)}
  .t-body{font-size:3.3px;fill:var(--grey)}
  .t-body-white{font-size:3.3px;fill:#fff}
  .t-label{font-size:3.5px;font-weight:700;fill:var(--blue)}
  .t-label-white{font-size:3.5px;font-weight:700;fill:#fff}
  .t-num{font-size:4px;font-weight:700;fill:#fff}
  .t-value{font-size:4.2px;fill:var(--grey)}
  .t-value-strong{font-size:4.2px;font-weight:700;fill:var(--blue)}
  .brand{font-size:7px;font-weight:600;fill:var(--blue);letter-spacing:.2px}
  .brand-lg{font-size:11px;font-weight:600;fill:var(--blue);letter-spacing:.3px}
  .copy{font-size:3.8px;fill:var(--grey)}
  .hero{font-size:13px;font-weight:700;fill:#fff}
  .fill-blue{fill:var(--blue)}
  .fill-grey{fill:var(--grey)}
  .fill-grey-mid{fill:var(--grey-mid)}
  .fill-grey-light{fill:var(--grey-light)}
  .fill-band{fill:var(--band)}
  .line-grey{stroke:var(--grey-light);stroke-width:.5;fill:none}
  .line-blue{stroke:var(--blue);stroke-width:.6;fill:none}
  .veil{fill:#fff;opacity:.82}
  .veil-soft{fill:#fff;opacity:.35}
</style>
</head>
<body>
<main class="deck">

  <!-- Cover -->
  <section class="slide col-1 row-1">
    <div class="photo" role="img" aria-label="City skyline photo with cable-stayed bridge under a blue sky"></div>
    <svg viewBox="0 0 294 165" width="294" height="165">
      <polygon class="veil-soft" points="230,0 294,0 294,165 120,165"/>
      <polygon class="veil" points="294,40 294,165 150,165"/>
      <text class="hero" x="14" y="133">Company Presentation</text>
      <text class="brand-lg" x="175" y="155">Brevora Holdings</text>
    </svg>
  </section>

  <!-- At a glance -->
  <section class="slide col-2 row-1">
    <div class="photo photo--sky" role="img" aria-label="Photo of a clear bubble floating in a cloudy blue sky"></div>
    <svg viewBox="0 0 294 165" width="294" height="165">
      <rect class="fill-blue" x="14" y="11" width="20" height="1.2"/>
      <text class="t-title" x="14" y="24"><tspan class="accent">Brevora</tspan> At Glance</text>
      <text class="t-sub" x="14" y="32">Insert some short and brief explanatory text about</text>
      <text class="t-sub" x="14" y="38">title here</text>
      <text class="t-body" x="14" y="57">Brief overview of our firm and the</text>
      <text class="t-body" x="14" y="62">advice we give to listed companies</text>
      <text class="t-body" x="14" y="67">and to investors across the region.</text>
      <rect class="fill-band" x="14" y="75" width="120" height="18"/>
      <text class="t-body-white" x="74" y="83" text-anchor="middle">Key message placed here for focus</text>
      <text class="t-body-white" x="74" y="88" text-anchor="middle">on safety and steady growth.</text>
      <text class="t-body" x="14" y="103">Further notes on our team and the</text>
      <text class="t-body" x="14" y="108">value we bring to each client.</text>
      <text class="brand" x="8" y="159">Brevora Holdings</text>
      <text class="copy" x="212" y="158">© Brevora Holdings 2017</text>
      <rect class="fill-blue" x="272" y="151" width="1.2" height="9"/>
      <text class="copy" x="280" y="158">2</text>
    </svg>
  </section>

  <!-- Principles -->
  <section class="slide col-3 row-1">
    <svg viewBox="0 0 294 165" width="294" height="165">
      <rect class="fill-blue" x="12" y="11" width="20" height="1.2"/>
      <text class="t-title" x="12" y="24"><tspan class="accent">Team/Company</tspan> Principles</text>
      <text class="t-sub" x="12" y="32">Short team principles description</text>
      <g class="line-grey">
        <line x1="102" y1="62" x2="148" y2="88"/><line x1="102" y1="84" x2="148" y2="88"/>
        <line x1="102" y1="105" x2="148" y2="88"/><line x1="102" y1="127" x2="148" y2="88"/>
        <line x1="193" y1="62" x2="148" y2="88"/><line x1="193" y1="84" x2="148" y2="88"/>
        <line x1="193" y1="105" x2="148" y2="88"/><line x1="193" y1="127" x2="148" y2="88"/>
      </g>
      <circle class="fill-blue" cx="148" cy="88" r="24"/>
      <g class="fill-grey">
        <circle cx="102" cy="62" r="5"/><circle cx="102" cy="84" r="5"/><circle cx="102" cy="105" r="5"/><circle cx="102" cy="127" r="5"/>
        <circle cx="193" cy="62" r="5"/><circle cx="193" cy="84" r="5"/><circle cx="193" cy="105" r="5"/><circle cx="193" cy="127" r="5"/>
      </g>
      <g text-anchor="middle">
        <text class="t-num" x="102" y="63.5">01</text><text class="t-num" x="102" y="85.5">03</text>
        <text class="t-num" x="102" y="106.5">05</text><text class="t-num" x="102" y="128.5">07</text>
        <text class="t-num" x="193" y="63.5">02</text><text class="t-num" x="193" y="85.5">04</text>
        <text class="t-num" x="193" y="106.5">06</text><text class="t-num" x="193" y="128.5">08</text>
      </g>
      <g text-anchor="end">
        <text class="t-label" x="92" y="60">LOREM OPTION</text><text class="t-body" x="92" y="65">Short note on this principle</text>
        <text class="t-label" x="92" y="82">LOREM OPTION</text><text class="t-body" x="92" y="87">Short note on this principle</text>
        <text class="t-label" x="92" y="103">LOREM OPTION</text><text class="t-body" x="92" y="108">Short note on this principle</text>
        <text class="t-label" x="92" y="125">LOREM OPTION</text><text class="t-body" x="92" y="130">Short note on this principle</text>
      </g>
      <text class="t-label" x="203" y="60">LOREM OPTION</text><text class="t-body" x="203" y="65">Short note on this principle</text>
      <text class="t-label" x="203" y="82">LOREM OPTION</text><text class="t-body" x="203" y="87">Short note on this principle</text>
      <text class="t-label" x="203" y="103">LOREM OPTION</text><text class="t-body" x="203" y="108">Short note on this principle</text>
      <text class="t-label" x="203" y="125">LOREM OPTION</text><text class="t-body" x="203" y="130">Short note on this principle</text>
      <text class="brand" x="8" y="159">Brevora Holdings</text>
      <text class="copy" x="212" y="158">© Brevora Holdings 2017</text>
      <rect class="fill-blue" x="272" y="151" width="1.2" height="9"/>
      <text class="copy" x="280" y="158">3</text>
    </svg>
  </section>

  <!-- History -->
  <section class="slide col-4 row-1">
    <svg viewBox="0 0 294 165" width="294" height="165">
      <rect class="fill-blue" x="12" y="11" width="20" height="1.2"/>
      <text class="t-title" x="12" y="24"><tspan class="accent">Company</tspan> History</text>
      <text class="t-sub" x="12" y="32">Short time line description.</text>
      <rect class="fill-blue" x="20" y="92" width="258" height="6" rx="3"/>
      <g class="fill-grey">
        <circle cx="45" cy="95" r="6"/><circle cx="95" cy="95" r="6"/><circle cx="147" cy="95" r="6"/>
        <circle cx="200" cy="95" r="6"/><circle cx="255" cy="95" r="6"/>
      </g>
      <g fill="none" stroke="#fff" stroke-width=".7">
        <circle cx="45" cy="94" r="1.6"/><path d="M95 92 v6 M92 95 h6"/><path d="M145 97 l4 -4"/>
        <circle cx="200" cy="95" r="2.4"/><path d="M253 93 h4 v2 a2 2 0 0 1 -4 0z"/>
      </g>
      <g text-anchor="middle">
        <text class="t-value" x="45" y="107">2010</text>
        <text class="t-value" x="95" y="86">2011</text>
        <text class="t-value" x="147" y="107">2012</text>
        <text class="t-value" x="200" y="86">2013</text>
        <text class="t-value" x="255" y="107">2014</text>
        <text class="t-label" x="45" y="57">ESTABLISHMENT</text><text class="t-body" x="45" y="62">Brief note on this milestone</text>
        <text class="t-label" x="168" y="57">IT REGISTRATION</text><text class="t-body" x="168" y="62">Brief note on this milestone</text>
        <text class="t-label" x="258" y="57">TOP BRANDS LIST</text><text class="t-body" x="258" y="62">Brief note on this milestone</text>
        <text class="t-label" x="95" y="118">REFINEMENT</text><text class="t-body" x="95" y="123">Brief note on this milestone</text>
        <text class="t-label" x="225" y="118">HIGHER CAPABILITIES</text><text class="t-body" x="225" y="123">Brief note on this milestone</text>
        <text class="t-value" x="213" y="70">$100M IN</text><text class="t-value" x="213" y="75">REVENUE</text>
      </g>
      <path class="line-grey" d="M147 89 V80 H255 V89 M213 80 V77"/>
      <text class="brand" x="8" y="159">Brevora Holdings</text>
      <text class="copy" x="212" y="158">© Brevora Holdings 2017</text>
      <rect class="fill-blue" x="272" y="151" width="1.2" height="9"/>
      <text class="copy" x="280" y="158">4</text>
    </svg>
  </section>

  <!-- Showcase -->
  <section class="slide col-1 row-2">
    <svg viewBox="0 0 294 165" width="294" height="165">
      <rect class="fill-blue" x="14" y="11" width="20" height="1.2"/>
      <text class="t-title" x="14" y="24"><tspan class="accent">Project/Client</tspan> Showcase</text>
      <text class="t-sub" x="14" y="32">Short project description</text>
      <rect class="fill-band" x="20" y="50" width="170" height="34"/>
      <text class="t-label-white" x="26" y="60">CLIENT: LOREM COMPANY</text>
      <text class="t-body-white" x="26" y="68">Short summary of the client project</text>
      <text class="t-body-white" x="26" y="73">and the outcome we delivered.</text>
      <circle class="fill-blue" cx="30" cy="96" r="3.2"/>
      <circle class="fill-blue" cx="30" cy="109" r="3.2"/>
      <text class="t-body" x="37" y="97">Strategy short note on scope</text>
      <text class="t-body" x="37" y="110">Results short note on value</text>
      <line class="line-grey" x1="26" y1="120" x2="110" y2="120"/>
      <text class="t-body" x="26" y="127">Closing remark on the engagement</text>
      <text class="brand" x="8" y="159">Brevora Holdings</text>
      <text class="copy" x="212" y="158">© Brevora Holdings 2017</text>
      <rect class="fill-blue" x="272" y="151" width="1.2" height="9"/>
      <text class="copy" x="280" y="158">5</text>
    </svg>
    <div role="img" aria-label="Laptop displaying the client project" style="position:absolute;left:138px;top:54px;width:72px;height:76px;border-radius:3px;background:linear-gradient(180deg,#e8e8e8 0%,#cfcfcf 100%)"></div>
  </section>

  <!-- Section -->
  <section class="slide col-2 row-2">
    <div class="photo" role="img" aria-label="City skyline photo with cable-stayed bridge and highway"></div>
    <svg viewBox="0 0 294 165" width="294" height="165">
      <polygon class="veil-soft" points="190,0 294,0 294,165 100,165"/>
      <polygon class="veil" points="294,20 294,165 170,165"/>
      <text class="hero" x="10" y="28">Section Slide</text>
      <text class="brand-lg" x="175" y="155">Brevora Holdings</text>
    </svg>
  </section>

  <!-- Services -->
  <section class="slide col-3 row-2">
    <svg viewBox="0 0 294 165" width="294" height="165">
      <rect class="fill-blue" x="12" y="11" width="20" height="1.2"/>
      <text class="t-title" x="12" y="24"><tspan class="accent">Services</tspan> Show</text>
      <text class="t-sub" x="12" y="32">Short services description</text>
      <g class="fill-blue">
        <circle cx="50" cy="76" r="15"/><circle cx="115" cy="76" r="15"/><circle cx="179" cy="76" r="15"/><circle cx="246" cy="76" r="15"/>
      </g>
      <g fill="none" stroke="#fff" stroke-width=".9">
        <rect x="44" y="71" width="12" height="8"/><path d="M48 82 h4"/>
        <rect x="111" y="69" width="8" height="14" rx="1"/>
        <path d="M174 82 l9 -9 l2 2 l-9 9 z"/>
        <rect x="240" y="71" width="10" height="7"/><path d="M243 80 h9 v-6"/>
      </g>
      <g class="line-grey"><line x1="30" y1="101" x2="70" y2="101"/><line x1="95" y1="101" x2="135" y2="101"/><line x1="159" y1="101" x2="199" y2="101"/><line x1="226" y1="101" x2="266" y2="101"/></g>
      <g text-anchor="middle">
        <text class="t-label" x="50" y="106">DESIGN &amp; DEV</text>
        <text class="t-label" x="115" y="106">MOBILE APPS</text>
        <text class="t-label" x="179" y="106">COPYWRITING</text>
        <text class="t-label" x="246" y="106">SOCIAL MARKETING</text>
        <text class="t-body" x="50" y="116">Short text on this service</text>
        <text class="t-body" x="115" y="116">Short text on this service</text>
        <text class="t-body" x="179" y="116">Short text on this service</text>
        <text class="t-body" x="246" y="116">Short text on this service</text>
      </g>
      <text class="brand" x="8" y="159">Brevora Holdings</text>
      <text class="copy" x="212" y="158">© Brevora Holdings 2017</text>
      <rect class="fill-blue" x="272" y="151" width="1.2" height="9"/>
      <text class="copy" x="280" y="158">6</text>
    </svg>
  </section>

  <!-- Revenue -->
  <section class="slide col-4 row-2">
    <svg viewBox="0 0 294 165" width="294" height="165">
      <rect class="fill-blue" x="12" y="11" width="20" height="1.2"/>
      <text class="t-title" x="12" y="24"><tspan class="accent">Annual</tspan> Revenue</text>
      <text class="t-sub" x="12" y="32">Short financial results review</text>
      <text class="t-label" x="18" y="64">LOREM IPSUM TITLE</text>
      <text class="t-body" x="18" y="72">Summary of results for the year</text>
      <text class="t-body" x="18" y="77">with steady growth in revenue</text>
      <text class="t-body" x="18" y="82">across all advisory services.</text>
      <g opacity=".9">
        <polygon class="fill-grey-mid" points="108,132 132,76 156,132"/>
        <polygon class="fill-grey" points="134,132 156,88 178,132"/>
        <polygon class="fill-grey-mid" points="212,132 236,84 260,132"/>
        <polygon class="fill-grey" points="226,132 252,66 280,132"/>
      </g>
      <polygon class="fill-blue" points="160,132 184,60 210,132"/>
      <rect class="fill-blue" x="104" y="132" width="178" height="5" rx="2.5"/>
      <g text-anchor="middle">
        <text class="t-value" x="132" y="72">16.20%</text>
        <text class="t-value" x="156" y="84">14.22%</text>
        <text class="t-value-strong" x="184" y="56">18.2%</text>
        <text class="t-value" x="236" y="80">16.2%</text>
        <text class="t-value" x="252" y="62">17.62%</text>
        <text class="t-num" x="132" y="135.8" style="font-size:2.6px">2010</text>
        <text class="t-num" x="156" y="135.8" style="font-size:2.6px">2011</text>
        <text class="t-num" x="184" y="135.8" style="font-size:2.6px">2012</text>
        <text class="t-num" x="236" y="135.8" style="font-size:2.6px">2013</text>
        <text class="t-num" x="258" y="135.8" style="font-size:2.6px">2014</text>
      </g>
      <text class="brand" x="8" y="159">Brevora Holdings</text>
      <text class="copy" x="212" y="158">© Brevora Holdings 2017</text>
      <rect class="fill-blue" x="272" y="151" width="1.2" height="9"/>
      <text class="copy" x="280" y="158">7</text>
    </svg>
  </section>

  <!-- Global presence -->
  <section class="slide col-1 row-3">
    <div role="img" aria-label="World map in grey showing office locations" style="position:absolute;left:75px;top:44px;width:158px;height:78px;border-radius:6px;background:linear-gradient(180deg,#8c8c8c 0%,#a6a6a6 100%)"></div>
    <svg viewBox="0 0 294 165" width="294" height="165">
      <rect class="fill-blue" x="14" y="11" width="20" height="1.2"/>
      <text class="t-title" x="14" y="24"><tspan class="accent">Global</tspan> Presence</text>
      <text class="t-sub" x="14" y="32">Short description for the global presence.</text>
      <g class="line-grey" stroke="#9a9a9a">
        <line x1="59" y1="77" x2="100" y2="68"/><line x1="59" y1="120" x2="112" y2="104"/>
        <line x1="145" y1="113" x2="140" y2="70"/><line x1="184" y1="108" x2="160" y2="88"/>
        <line x1="242" y1="71" x2="200" y2="70"/><line x1="242" y1="120" x2="212" y2="106"/>
      </g>
      <g class="fill-blue">
        <circle cx="42" cy="77" r="17"/><circle cx="42" cy="120" r="17"/><circle cx="145" cy="126" r="16"/>
        <circle cx="184" cy="120" r="12"/><circle cx="259" cy="71" r="17"/><circle cx="259" cy="120" r="17"/>
      </g>
      <g text-anchor="middle">
        <text class="t-label-white" x="42" y="74">N. AMERICA</text><text class="t-body-white" x="42" y="80">Office note here</text>
        <text class="t-label-white" x="42" y="117">S. AMERICA</text><text class="t-body-white" x="42" y="123">Office note here</text>
        <text class="t-label-white" x="145" y="123">EUROPE</text><text class="t-body-white" x="145" y="129">Office note here</text>
        <text class="t-label-white" x="184" y="118">AFRICA</text><text class="t-body-white" x="184" y="124">Office note here</text>
        <text class="t-label-white" x="259" y="68">ASIA</text><text class="t-body-white" x="259" y="74">Office note here</text>
        <text class="t-label-white" x="259" y="117">OCEANIA</text><text class="t-body-white" x="259" y="123">Office note here</text>
      </g>
      <text class="brand" x="8" y="159">Brevora Holdings</text>
      <text class="copy" x="212" y="158">© Brevora Holdings 2017</text>
      <rect class="fill-blue" x="272" y="151" width="1.2" height="9"/>
      <text class="copy" x="280" y="158">8</text>
    </svg>
  </section>

  <!-- Puzzle -->
  <section class="slide col-2 row-3">
    <svg viewBox="0 0 294 165" width="294" height="165">
      <rect class="fill-blue" x="14" y="11" width="20" height="1.2"/>
      <text class="t-title" x="14" y="24"><tspan class="accent">Infographic</tspan> Puzzle</text>
      <text class="t-sub" x="14" y="32">Short description</text>
      <g transform="rotate(45 150 90)">
        <rect class="fill-blue" x="126" y="66" width="23" height="23"/>
        <rect class="fill-grey" x="151" y="66" width="23" height="23"/>
        <rect class="fill-grey-mid" x="126" y="91" width="23" height="23"/>
        <rect class="fill-grey-light" x="151" y="91" width="23" height="23"/>
      </g>
      <g class="fill-blue"><circle cx="168" cy="59" r="2.6"/><circle cx="180" cy="72" r="2.6"/></g>
      <g class="line-grey" stroke="#9a9a9a">
        <polyline points="80,58 140,58"/><polyline points="80,114 135,114"/>
        <polyline points="165,80 200,80"/><polyline points="160,126 200,126"/>
      </g>
      <text class="t-label" x="80" y="55">MARKETING</text><text class="t-body" x="30" y="64">Short note for this piece</text>
      <text class="t-label" x="80" y="111">SEARCH &amp; RESULTS</text><text class="t-body" x="30" y="120">Short note for this piece</text>
      <text class="t-label" x="204" y="78">KEY ACHIEVEMENTS</text><text class="t-body" x="204" y="86">Short note for this piece</text>
      <text class="t-label" x="204" y="124">FIRE AND LAUNCH</text><text class="t-body" x="204" y="132">Short note for this piece</text>
      <text class="brand" x="8" y="159">Brevora Holdings</text>
      <text class="copy" x="212" y="158">© Brevora Holdings 2017</text>
      <rect class="fill-blue" x="272" y="151" width="1.2" height="9"/>
      <text class="copy" x="280" y="158">9</text>
    </svg>
  </section>

  <!-- Process -->
  <section class="slide col-3 row-3">
    <svg viewBox="0 0 294 165" width="294" height="165">
      <rect class="fill-blue" x="12" y="11" width="20" height="1.2"/>
      <text class="t-title" x="12" y="24"><tspan class="accent">Services</tspan> Process</text>
      <text class="t-sub" x="12" y="32">Short description</text>
      <g fill="none" stroke-width="9">
        <path d="M50 92 A20 20 0 0 1 90 92" stroke="var(--grey)"/>
        <path d="M90 92 A20 20 0 0 0 130 92" stroke="var(--blue)"/>
        <path d="M130 92 A20 20 0 0 1 170 92" stroke="var(--blue-soft)"/>
        <path d="M170 92 A20 20 0 0 0 210 92" stroke="var(--grey-light)"/>
        <path d="M210 92 A20 20 0 0 1 250 92" stroke="var(--grey-light)"/>
      </g>
      <circle class="fill-blue" cx="50" cy="96" r="1.8"/><circle class="fill-blue" cx="250" cy="96" r="1.8"/>
      <g fill="none" stroke-width=".8">
        <circle cx="70" cy="94" r="3.5" stroke="var(--grey)"/>
        <circle cx="110" cy="88" r="3.5" stroke="var(--blue)"/>
        <circle cx="150" cy="94" r="3.5" stroke="var(--blue)"/>
        <rect x="186" y="85" width="8" height="6" stroke="var(--grey)"/>
        <path d="M225 92 h8 v-5 h-8 z M233 89 h3 l2 3 h-5" stroke="var(--grey)"/>
      </g>
      <g text-anchor="middle">
        <text class="t-label-white" x="70" y="73.5" style="font-size:2.8px">CREATIVE IDEA</text>
        <text class="t-label-white" x="110" y="111.5" style="font-size:2.8px">RESEARCH</text>
        <text class="t-label-white" x="150" y="73.5" style="font-size:2.8px">CONCEPT</text>
        <text class="t-label" x="190" y="111.5" style="font-size:2.8px">DESIGN</text>
        <text class="t-label" x="230" y="73.5" style="font-size:2.8px">DELIVERY</text>
        <text class="t-label" x="50" y="103" style="font-size:2.8px">START</text>
        <text class="t-label" x="250" y="103" style="font-size:2.8px">FINISH</text>
        <text class="t-body" x="110" y="58">Short note on this step</text>
        <text class="t-body" x="190" y="58">Short note on this step</text>
        <text class="t-body" x="70" y="124">Short note on this step</text>
        <text class="t-body" x="150" y="124">Short note on this step</text>
        <text class="t-body" x="230" y="124">Short note on this step</text>
      </g>
      <text class="brand" x="8" y="159">Brevora Holdings</text>
      <text class="copy" x="212" y="158">© Brevora Holdings 2017</text>
      <rect class="fill-blue" x="272" y="151" width="1.2" height="9"/>
      <text class="copy" x="277" y="158">10</text>
    </svg>
  </section>

  <!-- Closing -->
  <section class="slide col-4 row-3">
    <div class="photo" role="img" aria-label="City skyline photo with cable-stayed bridge by the river"></div>
    <svg viewBox="0 0 294 165" width="294" height="165">
      <polygon class="veil-soft" points="240,0 294,0 294,165 150,165"/>
      <polygon class="veil" points="294,50 294,165 165,165"/>
      <text class="hero" x="10" y="133" style="font-size:12px">Thank you for your time</text>
      <text class="brand-lg" x="175" y="155">Brevora Holdings</text>
    </svg>
  </section>

</main>
</body>
</html>
```